Fresh web design for high profile Golf Club

We need an exciting web site that serves both members and visitors. Our current site has the relevant sections and pages but lacks a visual impact. There are a number of very good looking golf websites out there and we want to look the best.
We need a site that will attract golfers from all over Australia to come to our course to enjoy one of the finest 36 hole championship courses as well as fantastic clubhouse facilities on their next golfing holiday.
The member section needs to provide relevant information pages and regular news and event updates to 3000 members. We are situated on the Murray River with over 300 days of sunshine and ideal golfing weather every year.
We would like to stay with our existing logo and colours as a theme.

Target Market(s)

Golfers looking for golf holiday packages.

Industry/Entity Type

Club

Requirements
Must have
• Must have contact number for golf package holidays. Must have button for member entry and button for visitor entry. Existing site is www.kelvaronegolf.com.au. Looking for a big improvement in the look of the home page.
Nice to have
• Would like constantly updated weather reporting from source such as weather channel.

```html
<!DOCTYPE html>
<html lang="en">
<head>
<meta charset="utf-8">
<title>Kelvarone Golf Club</title>
<link rel="stylesheet" href="https://fonts.googleapis.com/css2?family=Cabin:wght@400;500;600&display=swap">
<style>
:root{
  --green:#8cbf3f;
  --green-dark:#6f9f28;
  --teal:#4fb7c6;
  --orange:#f7a81b;
  --ink:#3d3d3d;
  --muted:#5a5a5a;
  --blue:#2a9fd0;
  --panel:rgba(255,255,255,0.72);
  --white:#ffffff;
}
*{box-sizing:border-box;margin:0;padding:0}
html,body{width:724px;height:1200px;overflow:hidden}
body{position:relative;font-family:"Cabin",sans-serif;color:var(--ink);font-size:11px}
.backdrop{position:absolute;inset:0;background:linear-gradient(180deg,#c9dfe9 0%,#d7e5ea 30%,#b7cba0 55%,#7fa14a 75%,#5c8a2c 100%)}
.backdrop-ball{position:absolute;left:0;top:700px;width:400px;height:380px;border-radius:50%;background:radial-gradient(circle at 45% 40%,rgba(255,255,255,.85),rgba(220,225,228,.5) 60%,rgba(200,210,210,0) 72%)}
.member-bar{position:absolute;left:404px;top:0;width:241px;height:44px;background:var(--green);border-radius:0 0 6px 6px;display:flex;align-items:center;justify-content:center;gap:14px;color:var(--white);font-size:12px}
.member-bar span{display:flex;align-items:center;gap:5px}
.member-bar .divider{width:1px;height:14px;background:rgba(255,255,255,.7)}
.brand{position:absolute;left:80px;top:64px;display:flex;align-items:center;gap:12px}
.brand-dot{width:52px;height:52px;border-radius:50%;background:var(--green)}
.brand-name{font-size:22px;font-weight:400;color:#4a4a4a}
.main-nav{position:absolute;left:332px;top:88px;display:flex;gap:6px;font-size:12px;color:#333}
.main-nav a{padding:3px 6px;color:inherit;text-decoration:none}
.main-nav a.active{background:var(--green);color:var(--white);border-radius:4px}
.package-phone{position:absolute;right:79px;top:58px;font-size:11px;color:var(--muted);display:flex;align-items:center;gap:5px}
.package-phone b{color:var(--green-dark);font-weight:600}
.hero{position:absolute;left:77px;top:137px;width:570px;height:323px;border-radius:6px;overflow:hidden;border:2px solid #fff}
.hero-photo{position:absolute;inset:0;background:linear-gradient(180deg,#5f9fd9 0%,#a9cde8 25%,#7faa4c 42%,#5d8c24 65%,#3e6a15 100%)}
.hero-card{position:absolute;left:68px;top:75px;width:250px;height:178px;background:rgba(255,255,255,.32);border-radius:6px;padding:18px 14px;color:var(--white)}
.hero-card h1{font-size:22px;font-weight:400;line-height:1.1;margin-bottom:12px}
.hero-card p{font-size:8.5px;line-height:1.35;margin-bottom:12px}
.btn-orange{display:inline-block;background:var(--orange);color:var(--white);font-size:10px;font-weight:600;padding:6px 12px;border-radius:4px}
.hero-arrow{position:absolute;top:130px;width:48px;height:58px;background:#fff;display:flex;align-items:center;justify-content:center}
.hero-arrow.prev{left:0;border-radius:0 6px 6px 0}
.hero-arrow.next{right:0;border-radius:6px 0 0 6px}
.tiles{position:absolute;left:77px;top:467px;display:flex;gap:12px}
.tile{width:182px;height:110px;border-radius:5px;overflow:hidden;position:relative}
.tile-photo{height:82px}
.tile-bar{position:absolute;left:0;right:0;bottom:0;height:28px;display:flex;align-items:center;justify-content:space-between;padding:0 8px;color:var(--white);font-size:12px}
.tile-bar span{display:flex;align-items:center;gap:5px}
.tile.packages .tile-bar{background:var(--green)}
.tile.holidays .tile-bar{background:var(--teal)}
.tile.news .tile-bar{background:var(--orange)}
.panel{position:absolute;left:77px;top:587px;width:570px;height:573px;background:var(--panel);border-radius:6px}
.panel h2{position:absolute;left:14px;top:22px;font-size:15px;font-weight:500;color:var(--green-dark)}
.photo{position:absolute;border-radius:6px;border:2px solid #fff}
.intro-photo{left:13px;top:60px;width:199px;height:130px;background:linear-gradient(180deg,#4e8a2e,#2f5e1a)}
.intro-text{position:absolute;left:222px;top:62px;width:335px;font-size:10.5px;line-height:1.62;color:var(--muted)}
.read-more{position:absolute;font-size:9px;color:var(--muted);display:flex;align-items:center;gap:3px}
.story h3{position:absolute;font-size:15px;font-weight:400;color:var(--green)}
.story p{position:absolute;width:230px;font-size:10.5px;line-height:1.6;color:var(--muted)}
.widget-head{position:absolute;left:387px;width:169px;height:24px;background:var(--green);border-radius:5px;color:var(--white);font-size:13px;display:flex;align-items:center;gap:5px;padding-left:8px}
.forecast{position:absolute;left:387px;top:277px;width:169px;display:flex;justify-content:space-between;text-align:center;font-size:10px}
.forecast div{width:56px}
.forecast .day{color:var(--muted);margin:2px 0}
.forecast .temp{color:var(--blue)}
.forecast .temp b{color:var(--ink);font-weight:400}
.quote{position:absolute;left:387px;display:flex;gap:8px}
.quote-photo{width:52px;height:50px;border-radius:4px;border:2px solid #fff;background:linear-gradient(180deg,#9aa3a8,#5b6266)}
.quote-name{color:var(--green-dark);font-size:9px;margin:12px 0 3px}
.quote-text{font-size:10.5px;line-height:1.5;color:var(--muted)}
.site-footer{position:absolute;left:0;right:0;top:1173px;text-align:center;color:var(--white);font-size:10px}
</style>
</head>
<body>
<div class="backdrop" role="img" aria-label="Blurred close-up of a golf ball resting on green fairway grass">
  <div class="backdrop-ball"></div>
</div>

<div class="member-bar">
  <span><svg width="10" height="10" viewBox="0 0 10 10"><circle cx="5" cy="3" r="2.4" fill="#fff"/><path d="M0.5 10a4.5 4 0 0 1 9 0z" fill="#fff"/></svg>Club Member Login</span>
  <i class="divider"></i>
  <span><svg width="9" height="11" viewBox="0 0 9 11"><rect x="0.5" y="4.5" width="8" height="6" rx="1" fill="#fff"/><path d="M2.3 4.5V3a2.2 2.2 0 0 1 4.4 0v1.5" stroke="#fff" stroke-width="1.3" fill="none"/></svg>Join Now!</span>
</div>

<header class="brand">
  <span class="brand-dot"></span>
  <span class="brand-name">Kelvarone Golf Club</span>
</header>

<p class="package-phone"><svg width="10" height="10" viewBox="0 0 10 10"><path d="M2 0.5 3.8 2.6 2.8 4a6 6 0 0 0 3.2 3.2L7.4 6.2 9.5 8 8.5 9.5C4.5 9.5 0.5 5.5 0.5 1.5z" fill="var(--green-dark)"/></svg>Golf Packages <b>03 5800 1234</b></p>

<nav class="main-nav">
  <a href="#">Home</a>
  <a href="#" class="active">Membership</a>
  <a href="#">Golf Packages</a>
  <a href="#">Kelvarone</a>
  <a href="#">Contact</a>
</nav>

<section class="hero">
  <div class="hero-photo" role="img" aria-label="Golf ball on grass in front of a green with a flag pin under a blue sky"></div>
  <div class="hero-card">
    <h1>“A great golf course, it’s just the beginning!”</h1>
    <p>Kelvarone Golf Club invites you to experience this exceptional sporting venue situated on Australia’s mighty Murray River.</p>
    <span class="btn-orange">READ MORE</span>
  </div>
  <div class="hero-arrow prev"><svg width="16" height="26" viewBox="0 0 16 26"><path d="M13 2 3 13l10 11" stroke="var(--green)" stroke-width="3.5" fill="none"/></svg></div>
  <div class="hero-arrow next"><svg width="16" height="26" viewBox="0 0 16 26"><path d="M3 2l10 11L3 24" stroke="var(--green)" stroke-width="3.5" fill="none"/></svg></div>
</section>

<section class="tiles">
  <div class="tile packages">
    <div class="tile-photo" role="img" aria-label="Golf club iron beside a golf ball under a blue sky" style="background:linear-gradient(180deg,#6fa9d8,#c9ad78)"></div>
    <div class="tile-bar"><span><svg width="12" height="16" viewBox="0 0 12 16"><circle cx="6" cy="2" r="1.8" fill="#fff"/><path d="M5 4h2l1 5-2 1 1 6H5l-1-5 1-3L2 3" stroke="#fff" stroke-width="1.2" fill="none"/></svg>Golf Packages</span><svg width="14" height="14" viewBox="0 0 14 14"><circle cx="7" cy="7" r="7" fill="#fff"/><path d="M4 7h5M7 4.5 9.5 7 7 9.5" stroke="var(--green)" stroke-width="1.6" fill="none"/></svg></div>
  </div>
  <div class="tile holidays">
    <div class="tile-photo" role="img" aria-label="Coastal island bay with turquoise water and hills" style="background:linear-gradient(180deg,#3a7fd0,#2b6ea8 50%,#3fa3a8)"></div>
    <div class="tile-bar"><span><svg width="14" height="14" viewBox="0 0 14 14"><path d="M7 14V6M7 6C5 3 2 3 1 5M7 6c2-3 5-3 6-1M7 6C6 3 7 1 9 1" stroke="#fff" stroke-width="1.4" fill="none"/></svg>Holidays</span><svg width="14" height="14" viewBox="0 0 14 14"><circle cx="7" cy="7" r="7" fill="#fff"/><path d="M4 7h5M7 4.5 9.5 7 7 9.5" stroke="var(--teal)" stroke-width="1.6" fill="none"/></svg></div>
  </div>
  <div class="tile news">
    <div class="tile-photo" role="img" aria-label="Gloved hand placing a golf ball on a tee" style="background:linear-gradient(180deg,#7fb0d8,#7aa944 60%,#4e7f22)"></div>
    <div class="tile-bar"><span><svg width="16" height="12" viewBox="0 0 16 12"><path d="M1 1h6v10H1zM9 1h6v10H9z" fill="#fff"/></svg>Latest News</span><svg width="14" height="14" viewBox="0 0 14 14"><circle cx="7" cy="7" r="7" fill="#fff"/><path d="M4 7h5M7 4.5 9.5 7 7 9.5" stroke="var(--orange)" stroke-width="1.6" fill="none"/></svg></div>
  </div>
</section>

<main class="panel">
  <h2>“A great golf course is just the beginning...”</h2>
  <div class="photo intro-photo" role="img" aria-label="Golfer in a cap following through on a swing"></div>
  <p class="intro-text">If you’re chasing that elusive Murray Cod, Waterskiing, Boating, Fishing, relaxing on a houseboat or sunbaking on our golden beaches, Kelvarone is the perfect place to base yourself for a Murray River break. We are central to all the Murray attractions as well as having over 350 golf holes within an hours drive. Social golfers are welcome here 7 days a week.</p>
  <span class="read-more" style="left:488px;top:186px">READ MORE <svg width="10" height="10" viewBox="0 0 14 14"><circle cx="7" cy="7" r="7" fill="var(--green)"/><path d="M4 7h5M7 4.5 9.5 7 7 9.5" stroke="#fff" stroke-width="1.8" fill="none"/></svg></span>

  <article class="story">
    <div class="photo" role="img" aria-label="Golfers walking down a fairway" style="left:14px;top:233px;width:111px;height:101px;background:linear-gradient(180deg,#8ab55a,#4f8a2a)"></div>
    <h3 style="left:138px;top:245px">Watch Nell Harrow</h3>
    <p style="left:138px;top:268px">There’s so much to do on the beautiful Murray River. Discover Kelvarone’s 36 Hole Championship Golf Course, glorious golden sandy beach-</p>
    <span class="read-more" style="left:299px;top:324px">READ MORE <svg width="10" height="10" viewBox="0 0 14 14"><circle cx="7" cy="7" r="7" fill="var(--green)"/><path d="M4 7h5M7 4.5 9.5 7 7 9.5" stroke="#fff" stroke-width="1.8" fill="none"/></svg></span>
  </article>

  <article class="story">
    <div class="photo" role="img" aria-label="Professional golfer finishing a swing" style="left:14px;top:373px;width:111px;height:101px;background:linear-gradient(180deg,#9fb58a,#4d7a32)"></div>
    <h3 style="left:138px;top:383px">Professional Golfer</h3>
    <p style="left:138px;top:405px">There’s so much to do on the beautiful Murray River. Discover Kelvarone’s 36 Hole Championship Golf Course, glorious golden sandy beach-</p>
    <p style="left:138px;top:470px">There’s so much to do on the beautiful Murray River. Discover Kelvarone’s 36 Hole Championship Golf Course, glorious golden sandy beach-</p>
    <span class="read-more" style="left:299px;top:537px">READ MORE <svg width="10" height="10" viewBox="0 0 14 14"><circle cx="7" cy="7" r="7" fill="var(--green)"/><path d="M4 7h5M7 4.5 9.5 7 7 9.5" stroke="#fff" stroke-width="1.8" fill="none"/></svg></span>
  </article>

  <aside>
    <div class="widget-head" style="top:238px"><svg width="14" height="14" viewBox="0 0 14 14"><circle cx="7" cy="7" r="3" fill="#fff"/><g stroke="#fff" stroke-width="1.4"><path d="M7 0v2.5M7 11.5V14M0 7h2.5M11.5 7H14M2 2l1.8 1.8M10.2 10.2 12 12M2 12l1.8-1.8M10.2 3.8 12 2"/></g></svg>Weather</div>
    <div class="forecast">
      <div>
        <svg width="40" height="30" viewBox="0 0 40 30"><circle cx="24" cy="11" r="8" fill="#f9b81f"/><path d="M8 27h22a6 6 0 0 0-2-11.5A8 8 0 0 0 13 17a5 5 0 0 0-5 10z" fill="#e6eef2" stroke="#c9d4da"/></svg>
        <p class="day">Saturday</p><p class="temp">17 C - <b>9 C</b></p>
      </div>
      <div>
        <svg width="40" height="30" viewBox="0 0 40 30"><circle cx="24" cy="10" r="8" fill="#f9b81f"/><path d="M8 23h22a6 6 0 0 0-2-11.5A8 8 0 0 0 13 13a5 5 0 0 0-5 10z" fill="#e6eef2" stroke="#c9d4da"/><path d="M15 25l-1 3M21 25l-1 3M27 25l-1 3" stroke="var(--blue)" stroke-width="1.5"/></svg>
        <p class="day">Sunday</p><p class="temp">9 C - <b>5 C</b></p>
      </div>
      <div>
        <svg width="40" height="30" viewBox="0 0 40 30"><circle cx="24" cy="11" r="8" fill="#f9b81f"/><path d="M8 27h22a6 6 0 0 0-2-11.5A8 8 0 0 0 13 17a5 5 0 0 0-5 10z" fill="#e6eef2" stroke="#c9d4da"/></svg>
        <p class="day">Monday</p><p class="temp">13C - <b>7 C</b></p>
      </div>
    </div>

    <div class="widget-head" style="top:369px"><svg width="14" height="13" viewBox="0 0 14 13"><path d="M1 1h12v8H6l-3 3V9H1z" fill="#fff"/></svg>What they say</div>
    <div class="quote" style="top:407px">
      <div class="quote-photo" role="img" aria-label="Portrait of a club visitor"></div>
      <div><p class="quote-name">Tom BRINLEY</p><p class="quote-text">“It’s just AWSOME.<br>Proffesional Course.”</p></div>
    </div>
    <div class="quote" style="top:480px">
      <div class="quote-photo" role="img" aria-label="Portrait of a club visitor"></div>
      <div><p class="quote-name">Leo MARSH</p><p class="quote-text">“I love this classe.<br>I could be pro!</p></div>
    </div>
  </aside>
</main>

<footer class="site-footer">Kelvarone Golf Club 2012 Copyright!</footer>
</body>
</html>
```